Tutoring Site Hero Image Design

Updated Hero Concept for BrightLanternLessons.com

Create a hero that communicates “high quality, in-person private tutoring for all ages,” with warmth, credibility, and a real-life feel. The hero should move away from generic stock photography and better reflect the moments that make our service different: tutors meeting students where they are, one-on-one engagement, and a range of ages.

What the New Hero Should Convey
1. In-person, private, one-on-one support
This is the core differentiator, so the visual should feel intimate, focused, and real. Avoid anything that resembles online learning settings or learning-center classrooms.

2. Coverage of age ranges without clutter
We serve elementary through college. We do not need multiple students in the hero, but the chosen student should not skew strongly to one age group. Aim for a middle-ground age that feels inclusive, for example a middle schooler or early high schooler.

3. Realistic, authentic moments
Use photography that feels candid and warm. Natural light, home settings, kitchen tables, quiet study nooks, or library corners work well. Avoid staged stock looks, harsh lighting, or exaggerated classroom setups.

Design the hero at 2400 × 1200 px, with the focal point on the right side, safe area leaving room on the left for a stacked headline and form.

Images that I've shared as just thought starters and do not need to be used in the design.

Font styles to use
Sans Serif

Colors
0054AA
0677BA
7BADD7
CADEEF
E8F1F8
EB3D1F
EC4F4E
F09395
F8D3D4
FCEDEE
6B429C
8869AF
B7A5CE
E3DAEB
F3F0F8

```html
<!DOCTYPE html>
<html lang="en">
<head>
<meta charset="utf-8">
<title>Bright Lantern Lessons – Local Tutors</title>
<link href="https://fonts.googleapis.com/css2?family=Lato:wght@400;700;900&display=swap" rel="stylesheet">
<style>
  :root {
    --blue: #0054AA;
    --blue-mid: #0677BA;
    --blue-soft: #7BADD7;
    --blue-pale: #CADEEF;
    --blue-mist: #E8F1F8;
    --red: #EB3D1F;
    --red-soft: #EC4F4E;
    --red-pale: #FCEDEE;
    --purple: #6B429C;
    --purple-mist: #F3F0F8;
    --ink: #222222;
    --ink-soft: #333333;
    --white: #ffffff;
    --arrow: #dcdcdc;
  }
  * { box-sizing: border-box; margin: 0; padding: 0; }
  html, body { width: 1200px; height: 1000px; overflow: hidden; background: var(--white); }
  body { position: relative; font-family: "Lato", Arial, sans-serif; color: var(--ink); }
  .abs { position: absolute; }

  /* Header */
  .brand { left: 172px; top: 38px; display: flex; align-items: center; gap: 7px; }
  .brand-dot { width: 14px; height: 14px; border-radius: 50%; background: var(--red); }
  .brand-name { font-size: 13.5px; font-weight: 700; color: var(--blue); line-height: 1; white-space: nowrap; }
  .nav { left: 376px; top: 38px; display: flex; align-items: center; gap: 19px; font-size: 11px; font-weight: 700; color: var(--ink-soft); white-space: nowrap; }
  .nav-item { display: flex; align-items: center; gap: 5px; }
  .header-phone { left: 943px; top: 40px; display: flex; align-items: center; gap: 6px; font-size: 11px; font-weight: 700; color: var(--blue); white-space: nowrap; }

  /* Hero copy */
  .hero-title { left: 102px; top: 195px; font-size: 32.5px; font-weight: 700; line-height: 38.5px; color: var(--ink); letter-spacing: -0.2px; }
  .hero-text { left: 102px; top: 322px; width: 368px; font-size: 11px; line-height: 14.2px; color: var(--ink-soft); letter-spacing: 0.15px; }
  .btn { top: 397px; height: 35px; border-radius: 18px; display: flex; align-items: center; justify-content: center; font-size: 10.5px; font-weight: 700; white-space: nowrap; }
  .btn-quote { left: 102px; width: 95px; border: 1.5px solid var(--red); color: var(--red); background: var(--white); }
  .btn-call { left: 214px; width: 130px; background: var(--blue); color: var(--white); }

  /* Hero media */
  .hero-photo { left: 527px; top: 99px; width: 573px; height: 411px; border-radius: 16px;
    background:
      radial-gradient(ellipse at 78% 30%, rgba(252,237,238,0.75) 0%, rgba(252,237,238,0) 45%),
      radial-gradient(ellipse at 35% 55%, rgba(0,84,170,0.45) 0%, rgba(0,84,170,0) 40%),
      linear-gradient(160deg, #e9ddd0 0%, #c9ab8c 45%, #8a6648 75%, #b48a63 100%); }
  .notch-top { left: 460px; top: 80px; width: 203px; height: 113px; background: var(--white); border-bottom-right-radius: 18px; }
  .notch-bottom { left: 932px; top: 415px; width: 220px; height: 130px; background: var(--white); border-top-left-radius: 18px; }
  .badge { border-radius: 14px; color: var(--white); font-weight: 700; display: flex; align-items: center; }
  .badge-blue { left: 476px; top: 99px; width: 162px; height: 71px; background: var(--blue); font-size: 9.5px; line-height: 12px; padding-left: 29px; padding-bottom: 8px; }
  .badge-red { left: 957px; top: 441px; width: 174px; height: 85px; background: var(--red); font-size: 11px; line-height: 13.5px; padding-left: 30px; padding-bottom: 8px; }

  /* Comparison */
  .section-title { left: 0; top: 598px; width: 1200px; text-align: center; font-size: 26px; font-weight: 900; color: var(--ink-soft); letter-spacing: -0.2px; }
  .compare-panel { left: 171px; top: 658px; width: 858px; height: 380px; border-radius: 18px; background: var(--blue-mist); }
  .compare-label { top: 684px; width: 378px; text-align: center; font-size: 24px; font-weight: 900; }
  .label-them { left: 195px; color: var(--ink-soft); }
  .label-us { left: 628px; color: var(--blue); }
  .card { top: 722px; width: 378px; height: 320px; border-radius: 14px; padding: 16px 15px; box-shadow: 0 3px 10px rgba(0,0,0,0.12); }
  .card-them { left: 195px; background: var(--white); color: var(--ink); }
  .card-us { left: 628px; background: var(--blue); color: var(--white); }
  .card-image { width: 348px; height: 189px; border-radius: 10px; }
  .card-them .card-image { background: linear-gradient(135deg, #8f8f8f, #dedede 55%, #6a6a6a); }
  .card-us .card-image { background: linear-gradient(135deg, #c89a72, #ecd9c2 50%, #7a5a44); }
  .card-title { margin-top: 14px; font-size: 18.5px; font-weight: 900; white-space: nowrap; }
  .card-text { margin-top: 12px; font-size: 11px; line-height: 15px; white-space: nowrap; }
  .vs { left: 585px; top: 897px; font-size: 22px; font-weight: 900; color: var(--ink-soft); }
  .arrow-btn { top: 887px; width: 26px; height: 26px; border-radius: 50%; background: var(--arrow); display: flex; align-items: center; justify-content: center; }
  .arrow-prev { left: 159px; }
  .arrow-next { left: 1015px; }
</style>
</head>
<body>

<header>
  <div class="abs brand">
    <span class="brand-dot"></span>
    <span class="brand-name">Bright Lantern Lessons</span>
  </div>
  <nav class="abs nav">
    <svg width="17" height="17" viewBox="0 0 17 17" aria-label="Home"><circle cx="8.5" cy="8.5" r="8.5" fill="#0054AA"/><path d="M4.5 8.5 L8.5 5 L12.5 8.5 V12 H9.8 V9.8 H7.2 V12 H4.5 Z" fill="#fff"/></svg>
    <span class="nav-item">Tutoring Services <svg width="9" height="6" viewBox="0 0 9 6"><path d="M1 1 L4.5 4.5 L8 1" stroke="#333" stroke-width="1.4" fill="none"/></svg></span>
    <span class="nav-item">Locations</span>
    <span class="nav-item">Resources <svg width="9" height="6" viewBox="0 0 9 6"><path d="M1 1 L4.5 4.5 L8 1" stroke="#333" stroke-width="1.4" fill="none"/></svg></span>
    <span class="nav-item">For Partners</span>
    <span class="nav-item">For Tutors</span>
  </nav>
  <div class="abs header-phone">
    <svg width="12" height="12" viewBox="0 0 24 24"><path fill="#0054AA" d="M6.6 10.8a15.1 15.1 0 0 0 6.6 6.6l2.2-2.2c.3-.3.7-.4 1-.2 1.1.4 2.3.6 3.6.6.6 0 1 .4 1 1V20c0 .6-.4 1-1 1A17 17 0 0 1 3 4c0-.6.4-1 1-1h3.5c.6 0 1 .4 1 1 0 1.3.2 2.5.6 3.6.1.3 0 .7-.2 1z"/></svg>
    (555) 214-3870
  </div>
</header>

<section class="hero">
  <h1 class="abs hero-title">Local Tutors.<br>1-on-1 Learning.<br>Real Results.</h1>
  <p class="abs hero-text">For over 20 years, Bright Lantern Lessons has introduced students and families in our communities to experienced, professional, independent tutors who offer individualized, student-centered support across all grades and subjects, from kindergarten through college.</p>
  <a class="abs btn btn-quote">Get a Quote</a>
  <a class="abs btn btn-call">Call (555) 306-1142</a>

  <div class="abs hero-photo" role="img" aria-label="Candid photo: a tutor and an early high-school student working one-on-one at a home kitchen table in warm natural light"></div>
  <div class="abs notch-top"></div>
  <div class="abs notch-bottom"></div>
  <div class="abs badge badge-blue">Personalized Tutoring.<br>Real Results.</div>
  <div class="abs badge badge-red">Tailored Learning for<br>Every Student</div>
</section>

<section class="compare">
  <h2 class="abs section-title">Where Traditional Tutoring Misses the Mark</h2>
  <div class="abs compare-panel"></div>
  <div class="abs compare-label label-them">THEM</div>
  <div class="abs compare-label label-us">US</div>

  <article class="abs card card-them">
    <div class="card-image" role="img" aria-label="Black and white photo of a frustrated student studying alone at a laptop"></div>
    <h3 class="card-title">Online-Only Tutoring</h3>
    <p class="card-text">It’s no secret that over-reliance on virtual learning in recent years</p>
  </article>

  <div class="abs vs">VS</div>

  <article class="abs card card-us">
    <div class="card-image" role="img" aria-label="A young student writing at home with a tutor beside her"></div>
    <h3 class="card-title">In-Person, 1-On-1 Tutoring</h3>
    <p class="card-text">Students thrive when learning happens in real life. Families connect</p>
  </article>

  <div class="abs arrow-btn arrow-prev"><svg width="8" height="10" viewBox="0 0 8 10"><path d="M6 1 L2 5 L6 9" stroke="#444" stroke-width="1.8" fill="none"/></svg></div>
  <div class="abs arrow-btn arrow-next"><svg width="8" height="10" viewBox="0 0 8 10"><path d="M2 1 L6 5 L2 9" stroke="#444" stroke-width="1.8" fill="none"/></svg></div>
</section>

</body>
</html>
```